"Quiet Meadow" Organic Grocery Retail Packaging

"Quiet Meadow" is retail brand for Indian organic food products in following categories
- Lentils (2 lb and 4 lb)
- Flours (2 lb and 4 lb)
- Spices (whole spices like Cumin seeds) (100 gms, 200 gms, 400 gms)
- Spice Powders (Powdered spices like Chili powder) (100 gms, 200 gms, 400 gms)
- Masala Mixes (spices mixed together such as Garam Masala) (100 gms, 200 gms, 400 gms)
- Flour (10 lb - No transparent front part in this)

We are looking for one package design (except 10 lb flour) that will work for all categories, differentiated by at least color.
- Reference for competitors: 31Kavelo.com

Industry/Entity Type

Grocery Store

Requirements
Must have
• - Package design must have transparent part in front to show product inside
• - Front and back design
• - KPTR Organic logo and Non GMO logo
• - Back - Bar code, Nutrition Facts etc.
Nice to have
• We have an old logo in the attached CDR file. It would be nice to have a newer/updated logo.

```html
<!DOCTYPE html>
<html lang="en">
<head>
<meta charset="utf-8">
<title>Quiet Meadow – Spice Pouches</title>
<link href="https://fonts.googleapis.com/css2?family=Cinzel:wght@600;700&family=Comfortaa:wght@500&family=Arimo:wght@700&display=swap" rel="stylesheet">
<style>
  :root{
    --stage:#6f6962;
    --ink:#161616;
    --white:#ffffff;
    --cumin-deep:#135a24;
    --cumin-main:#1f7d36;
    --cumin-band-edge:#8fcd5e;
    --cumin-band-mid:#eef4e6;
    --cumin-accent:#3f9a3a;
    --cumin-window-a:#8b8878;
    --cumin-window-b:#a9a594;
    --chili-deep:#6f0d0e;
    --chili-main:#a8191a;
    --chili-band-edge:#c2281f;
    --chili-band-mid:#f2dcd3;
    --chili-accent:#3f9a3a;
    --chili-window-a:#a41d14;
    --chili-window-b:#c4311f;
    --badge-blue:#2f62a8;
    --badge-green:#2d8a3a;
  }
  *{box-sizing:border-box;margin:0;padding:0}
  html,body{width:1200px;height:796px;overflow:hidden}
  body{background:var(--stage);position:relative;font-family:"Cinzel",serif}

  .pouch{
    position:absolute;top:86px;width:473px;height:591px;
    border-radius:6px 6px 14px 14px;
    background:
      repeating-linear-gradient(90deg,rgba(255,255,255,.07) 0 2px,transparent 2px 26px,rgba(0,0,0,.08) 26px 28px,transparent 28px 40px),
      linear-gradient(90deg,var(--deep),var(--main) 12%,var(--main) 88%,var(--deep));
  }
  .pouch--cumin{left:110px;--deep:var(--cumin-deep);--main:var(--cumin-main);--edge:var(--cumin-band-edge);--mid:var(--cumin-band-mid);--win-a:var(--cumin-window-a);--win-b:var(--cumin-window-b)}
  .pouch--chili{left:640px;--deep:var(--chili-deep);--main:var(--chili-main);--edge:var(--chili-band-edge);--mid:var(--chili-band-mid);--win-a:var(--chili-window-a);--win-b:var(--chili-window-b)}

  .pouch__seal{position:absolute;left:0;right:0;top:22px;height:1px;background:rgba(255,255,255,.18)}

  .brand{
    position:absolute;left:0;right:0;top:70px;
    display:flex;align-items:center;justify-content:center;gap:10px;
  }
  .brand__name{font-family:"Cinzel",serif;font-weight:700;font-size:34px;color:var(--white);letter-spacing:1px}
  .brand__dot{width:16px;height:16px;border-radius:50%;background:var(--white)}

  .label-band{
    position:absolute;left:0;right:0;top:195px;height:281px;
    background:linear-gradient(90deg,var(--edge),var(--mid) 35%,var(--mid) 65%,var(--edge));
    border-top:3px solid rgba(255,255,255,.7);
    border-bottom:3px solid rgba(255,255,255,.7);
  }
  .label-band__kicker{
    position:absolute;left:0;right:0;top:16px;text-align:center;
    font-family:"Comfortaa",sans-serif;font-weight:500;font-size:24px;color:var(--cumin-accent);
  }
  .label-band__title{
    position:absolute;left:0;right:0;top:48px;text-align:center;
    font-family:"Cinzel",serif;font-weight:700;font-size:32px;color:var(--ink);letter-spacing:.5px;
  }
  .window{
    position:absolute;left:61px;top:95px;width:344px;height:159px;border-radius:8px;
    background:radial-gradient(ellipse at 40% 45%,var(--win-b),var(--win-a));
    box-shadow:inset 0 0 0 1px rgba(0,0,0,.15);
  }
  .net-weight{
    position:absolute;left:165px;top:525px;
    font-family:"Arimo",sans-serif;font-weight:700;font-size:11px;color:rgba(255,255,255,.9);letter-spacing:.3px;
  }
  .badge-verified{position:absolute;left:334px;top:505px;width:41px;height:61px;border-radius:3px;background:var(--white);border:3px solid var(--badge-blue)}
  .badge-organic{position:absolute;left:383px;top:506px;width:56px;height:56px;border-radius:50%;background:var(--white);border:5px solid var(--badge-green)}
</style>
</head>
<body>
  <section class="pouch pouch--cumin">
    <div class="pouch__seal"></div>
    <div class="brand"><span class="brand__name">Quiet Meadow</span><span class="brand__dot"></span></div>
    <div class="label-band">
      <p class="label-band__kicker">Organic</p>
      <h2 class="label-band__title">CUMIN SEEDS</h2>
      <div class="window" role="img" aria-label="Clear window showing whole cumin seeds"></div>
    </div>
    <p class="net-weight">NET WT. 3.5 OZ (100 GM)</p>
    <div class="badge-verified" role="img" aria-label="Non-GMO verification badge"></div>
    <div class="badge-organic" role="img" aria-label="KPTR organic certification badge"></div>
  </section>

  <section class="pouch pouch--chili">
    <div class="pouch__seal"></div>
    <div class="brand"><span class="brand__name">Quiet Meadow</span><span class="brand__dot"></span></div>
    <div class="label-band">
      <p class="label-band__kicker">Organic</p>
      <h2 class="label-band__title">CHILI POWDER</h2>
      <div class="window" role="img" aria-label="Clear window showing red chili powder"></div>
    </div>
    <p class="net-weight">NET WT. 3.5 OZ (100 GM)</p>
    <div class="badge-verified" role="img" aria-label="Non-GMO verification badge"></div>
    <div class="badge-organic" role="img" aria-label="KPTR organic certification badge"></div>
  </section>
</body>
</html>
```